Lumo4Kart - a fintech company - business card

We need a business card design for our Payments Technology company in Sydney, Australia. We provide business with payment solutions expanding across EFTPOS machines, online payment gateways and mobile payment solutions. We would like to see designs that are clean, classy and professional.
Target Market(s)
Business professionals, executives, c-suite
Industry/Entity Type
Fintech
Contact Information for Business Card
Will be on 400gsm. Logo will most likely be spot gloss unless designer recommends otherwise.
Font styles to use
Sans Serif
Requirements
Must have
- We need our website (lumo4kart.com.au), email (contact@lumo4kart.com.au), mobile (0432 587 904) and direct phone number (02 6815 3927) to feature on the card along with our logo (attached) and the words "EFTPOS | ONLINE | MOBILE"
- Font = Roboto

```html
<!DOCTYPE html>
<html lang="en">
<head>
<meta charset="UTF-8">
<title>Lumo4Kart Business Card</title>
<link href="https://fonts.googleapis.com/css2?family=Roboto:wght@400;500;700&display=swap" rel="stylesheet">
<style>
  :root {
    --stage: #2b2b2d;
    --card-white: #ffffff;
    --card-grey: #6b6c70;
    --back-grey: #646a72;
    --brand-blue: #155f95;
    --logo-grey: #6a6b6e;
    --text-light: #ffffff;
  }
  * { margin: 0; padding: 0; box-sizing: border-box; }
  html, body {
    width: 1200px; height: 801px; overflow: hidden;
    background: var(--stage);
    font-family: "Roboto", sans-serif;
  }
  .stage {
    width: 1200px; height: 801px;
    display: flex; flex-direction: column;
    align-items: center; justify-content: center; gap: 44px;
  }
  .card {
    position: relative;
    width: 540px; height: 310px;
    overflow: hidden;
    box-shadow: 0 10px 28px rgba(0,0,0,0.45);
  }

  /* Back side */
  .card-back { background: var(--back-grey); }
  .back-ring {
    position: absolute; left: 150px; top: 15px;
    width: 280px; height: 280px; border-radius: 50%;
    background: rgba(90, 105, 122, 0.55);
  }
  .back-brand {
    position: absolute; inset: 0;
    display: flex; flex-direction: column;
    align-items: center; justify-content: center;
    color: var(--text-light);
  }
  .back-name { font-size: 38px; font-weight: 700; letter-spacing: 0.5px; }
  .back-tagline { margin-top: 6px; font-size: 13px; font-weight: 400; letter-spacing: 1px; }

  /* Front side */
  .card-front { background: var(--card-white); }
  .front-wave { position: absolute; inset: 0; }
  .front-logo {
    position: absolute; left: 52px; top: 62px;
    display: flex; align-items: center; gap: 14px;
  }
  .logo-dot {
    width: 30px; height: 30px; border-radius: 50%;
    background: var(--brand-blue);
  }
  .logo-name {
    font-size: 36px; font-weight: 700; color: var(--logo-grey);
    letter-spacing: 0.5px;
  }
  .front-contact {
    position: absolute; right: 36px; bottom: 24px;
    text-align: right; color: var(--text-light);
  }
  .person-name { font-size: 21px; font-weight: 700; letter-spacing: 0.5px; line-height: 25px; }
  .person-title { font-size: 13px; font-weight: 500; line-height: 16px; margin-bottom: 12px; }
  .contact-list { list-style: none; }
  .contact-item {
    display: flex; justify-content: flex-end; align-items: center;
    gap: 8px; font-size: 13px; line-height: 19px;
  }
  .contact-icon { width: 12px; height: 12px; fill: var(--text-light); }
</style>
</head>
<body>
<main class="stage">

  <section class="card card-back" aria-label="Business card back">
    <div class="back-ring"></div>
    <div class="back-brand">
      <div class="back-name">LUMO4KART</div>
      <div class="back-tagline">EFTPOS | ONLINE | MOBILE</div>
    </div>
  </section>

  <section class="card card-front" aria-label="Business card front">
    <svg class="front-wave" viewBox="0 0 540 310" preserveAspectRatio="none">
      <path d="M0,105 C60,190 140,230 220,222 C300,214 340,110 420,92 C470,82 510,100 540,130"
            fill="none" stroke="var(--brand-blue)" stroke-width="9"/>
      <path d="M0,125 C60,210 140,248 222,240 C305,232 345,130 422,112 C472,102 512,118 540,146 L540,310 L0,310 Z"
            fill="var(--card-grey)"/>
    </svg>

    <div class="front-logo">
      <span class="logo-dot"></span>
      <span class="logo-name">LUMO4KART</span>
    </div>

    <div class="front-contact">
      <div class="person-name">DANIEL HAYES</div>
      <div class="person-title">CEO/FOUNDER</div>
      <ul class="contact-list">
        <li class="contact-item">02 6815 3927
          <svg class="contact-icon" viewBox="0 0 24 24"><path d="M6.6 10.8a15.1 15.1 0 0 0 6.6 6.6l2.2-2.2a1 1 0 0 1 1-.25 11.4 11.4 0 0 0 3.6.57 1 1 0 0 1 1 1V20a1 1 0 0 1-1 1A17 17 0 0 1 3 4a1 1 0 0 1 1-1h3.5a1 1 0 0 1 1 1c0 1.25.2 2.45.57 3.6a1 1 0 0 1-.25 1z"/></svg>
        </li>
        <li class="contact-item">0432 587 904
          <svg class="contact-icon" viewBox="0 0 24 24"><path d="M7 1h10a2 2 0 0 1 2 2v18a2 2 0 0 1-2 2H7a2 2 0 0 1-2-2V3a2 2 0 0 1 2-2zm0 3v15h10V4z"/></svg>
        </li>
        <li class="contact-item">contact@lumo4kart.com.au
          <svg class="contact-icon" viewBox="0 0 24 24"><path d="M2 5h20v14H2zm2 2v.5l8 5 8-5V7z"/></svg>
        </li>
        <li class="contact-item">www.lumo4kart.com.au
          <svg class="contact-icon" viewBox="0 0 24 24"><circle cx="12" cy="12" r="10"/></svg>
        </li>
      </ul>
    </div>
  </section>

</main>
</body>
</html>
```